Colorful logo using law firm name. letterhead Quillon Law national consumer fraud.

We only bring consumer fraud litigation against fortune 50 companies across the United States

Reason: I want 1 day extension not 5. Being new at this, I want my letterhead to match everything else. Sorry for creating confusion.

Please review all my updates and pictures. If someone knows how to tell me I can get the webpage done. Change: 4 offiecs: Cal, NC, AL, and MS. I have numbers for each for website except MS. I want pictures, many I have uploaded. Need office picttures, Downtown SF, etc. I have provided info for my the "about the firm" (mostly me), investigations, and representative cases. The main page should be be big city perferably SF, whcih I sent picture. Also, inside and out of offices that I have uploaded. On website, I hope to list the addres and phone number for each locatiom. Thank you for yoru patience.

Law Firm

```html
<!DOCTYPE html>
<html lang="en">
<head>
<meta charset="utf-8">
<title>Quillon Law PC — Letterhead</title>
<link rel="stylesheet" href="https://fonts.googleapis.com/css2?family=Exo+2:wght@300;400;500;600&family=Montserrat:wght@600&display=swap">
<style>
  :root {
    --olive: #7d7860;
    --red: #ec4a33;
    --white: #ffffff;
    --paper: #ffffff;
    --faint: #fadcd7;
  }
  * { margin: 0; padding: 0; box-sizing: border-box; }
  html, body { width: 848px; height: 1200px; overflow: hidden; background: var(--paper); }
  .letterhead {
    position: relative; width: 848px; height: 1200px;
    background: var(--paper); overflow: hidden;
    font-family: "Exo 2", sans-serif; color: var(--white);
  }
  .tagline-band {
    position: absolute; left: 0; top: 0; width: 100%; height: 50px;
    background: var(--olive);
  }
  .tagline {
    position: absolute; left: 31px; top: 22px;
    font-family: "Montserrat", sans-serif; font-weight: 600;
    font-size: 16px; letter-spacing: 0.2px; line-height: 1;
  }
  .brand-band {
    position: absolute; left: 0; top: 50px; width: 100%; height: 121px;
    background: var(--red);
  }
  .brand-rule {
    position: absolute; left: 0; top: 171px; width: 100%; height: 16px;
    background: var(--olive);
  }
  .brand-name {
    position: absolute; left: 28px; top: 22px;
    font-weight: 300; font-size: 74px; line-height: 1;
    letter-spacing: 1px; color: var(--white); white-space: nowrap;
  }
  .attorney {
    position: absolute; right: 28px; top: 72px; text-align: right;
    line-height: 1;
  }
  .attorney-name { font-weight: 600; font-size: 16px; letter-spacing: 0.6px; }
  .attorney-title { font-weight: 400; font-size: 12px; margin-top: 5px; letter-spacing: 0.4px; }
  .attorney-contact { font-weight: 400; font-size: 11.5px; letter-spacing: 0.6px; margin-top: 14px; line-height: 17px; }
  .watermark {
    position: absolute; left: 0; right: 0; top: 560px; text-align: center;
    font-weight: 300; font-size: 76px; line-height: 1; letter-spacing: 1px;
    color: var(--faint); white-space: nowrap;
  }
  .offices {
    position: absolute; left: 0; top: 1057px; width: 100%; height: 83px;
    background: var(--olive);
  }
  .office { position: absolute; top: 5px; font-size: 10.5px; letter-spacing: 0.7px; line-height: 18.5px; font-weight: 500; }
  .office-state { font-weight: 600; }
  .office--ca { left: 28px; }
  .office--al { left: 214px; }
  .office--nc { left: 446px; }
  .office--ms { left: 691px; }
  .office-divider { position: absolute; top: 9px; width: 1.5px; height: 66px; background: var(--red); }
  .office-divider--1 { left: 197px; }
  .office-divider--2 { left: 432px; }
  .office-divider--3 { left: 677px; }
  .web-band {
    position: absolute; left: 0; top: 1140px; width: 100%; height: 26px;
    background: var(--red); text-align: center;
    font-size: 11.5px; font-weight: 600; letter-spacing: 3px; line-height: 26px;
  }
  .web-sep { margin: 0 14px; }
  .license-band {
    position: absolute; left: 0; top: 1166px; width: 100%; height: 34px;
    background: var(--olive); text-align: center;
    font-size: 13px; font-weight: 500; letter-spacing: 1.3px; line-height: 32px;
  }
</style>
</head>
<body>
<div class="letterhead">
  <header>
    <div class="tagline-band"><p class="tagline">A NATIONAL CONSUMER CLASS ACTION FIRM</p></div>
    <div class="brand-band">
      <div class="brand-name">QUILLON LAW</div>
    </div>
    <div class="attorney">
      <div class="attorney-name">M. Daniel Quillon</div>
      <div class="attorney-title">Attorney</div>
      <div class="attorney-contact">daniel@quillonlawpc.com<br>205/555-0187 (cell)</div>
    </div>
    <div class="brand-rule"></div>
  </header>

  <div class="watermark" aria-hidden="true">QUILLON LAW</div>

  <footer>
    <div class="offices">
      <div class="office office--ca">
        <div class="office-state">CALIFORNIA</div>
        <div>318 Harlan Street</div>
        <div>San Francisco, CA 94111</div>
        <div>415/555-0142 (Tel)</div>
      </div>
      <div class="office-divider office-divider--1"></div>
      <div class="office office--al">
        <div class="office-state">ALABAMA</div>
        <div>740 Linden Avenue South, Suite 210</div>
        <div>Birmingham, AL 35205</div>
        <div>205/555-0163 (Tel)</div>
      </div>
      <div class="office-divider office-divider--2"></div>
      <div class="office office--nc">
        <div class="office-state">NORTH CAROLINA</div>
        <div>4120 Maple Crest Road, Third Floor</div>
        <div>Charlotte, NC 28209</div>
        <div>704/555-0126 (Tel)</div>
      </div>
      <div class="office-divider office-divider--3"></div>
      <div class="office office--ms">
        <div class="office-state">MISSISSIPPI</div>
        <div>Post Office Box</div>
        <div>Meridian, MS</div>
        <div>205/555-0187 (Tel)</div>
      </div>
    </div>
    <div class="web-band">www.quillonlawpc.com<span class="web-sep">|</span>www.consumerjustice.lawyer</div>
    <div class="license-band">Licensed in California (318406), Alabama (ASB-4821-Q72K), Mississippi (20473)</div>
  </footer>
</div>
</body>
</html>
```